Leading In-Home Tutoring Company Needs Web Banners

We need a suite of web banners for our re-marketing campaign. We are based in Melbourne and heading into the busiest time of the year with back to school and we would like to help guide parents to working with us via quality designed banners with the right CTAs. Banner specs as follows (W x H in pixels)
Medium Rectangle: 300 x 250
Vertical rectangle: 240 x 400
Banner: 468 x 60
Leaderboard: 728 x 90
Square: 250 x 250
Mobile leaderboard: 320 x 50
Updates

Hi designers I'm new to this and didn't realise that I had to upload all files at the beginning. I have images that can be used for this project. Just need to work out how to upload them. Added Sunday, January 22, 2017

Hi awesome designers... I've updated the brief now with new files :)

Target Market(s)

Mothers who value kids education. Our customer can be found having morning coffee with friends in her lycra as she prepares to go to the gym. Middle class, inner city and suburban Mums. Most likely on Friendnook.

Industry/Entity Type

It Company

Font styles to use
Sans Serif

Colors
0692cd
fbed22
f47f39
ec1f27

Requirements
Must have
• Wording should include.
• What we do: 1:1, In-Home Tutoring
• Value proposition: The Best Tutor For Your Child
• Call to Action - Free Assessment > Find Out More
• Adjusted layout to suit the sizes. Use of image where possible to provide immediate graphic display of what we do
Nice to have
• Keep it simple, create an emotive connection. Kids matter to parents and they will pay for services if we can create banners that show we care and can help wtih their education.
Should not have
• Anything negative or use fear marketing

```html
<!DOCTYPE html>
<html lang="en">
<head>
<meta charset="utf-8">
<title>Kestrel Study Web Banner Suite</title>
<link href="https://fonts.googleapis.com/css2?family=Roboto:ital,wght@0,500;0,700;0,900;1,700;1,900&display=swap" rel="stylesheet">
<style>
  :root {
    --yellow: #f6e62a;
    --blue: #0692cd;
    --sky: #23a7e2;
    --orange: #f47f39;
    --red: #ec1f27;
    --white: #ffffff;
    --page: #ffffff;
  }
  * { box-sizing: border-box; margin: 0; padding: 0; }
  html, body { width: 1200px; height: 756px; overflow: hidden; background: var(--page); }
  body { position: relative; font-family: "Roboto", Arial, sans-serif; }

  .banner {
    position: absolute;
    background: var(--yellow);
    overflow: hidden;
    box-shadow: 0 10px 18px rgba(0,0,0,0.18);
  }
  .banner--vertical   { left: 101px; top: 61px;  width: 241px; height: 401px; }
  .banner--square     { left: 444px; top: 61px;  width: 251px; height: 250px; }
  .banner--medium     { left: 797px; top: 61px;  width: 302px; height: 250px; }
  .banner--mobile     { left: 777px; top: 382px; width: 322px; height: 50px; }
  .banner--standard   { left: 627px; top: 484px; width: 471px; height: 60px; }
  .banner--leader     { left: 365px; top: 605px; width: 733px; height: 90px; }

  .logo-tab {
    position: absolute; top: 0; width: 112px; height: 111px;
    background: var(--white);
    border-radius: 0 0 56px 56px;
    text-align: center;
  }
  .brand {
    position: absolute;
    font-weight: 700; color: var(--blue);
    white-space: nowrap;
  }
  .brand--center { left: 0; right: 0; text-align: center; }
  .tagline {
    position: absolute; left: 0; right: 0;
    font-weight: 900; font-style: italic; font-size: 11.5px; line-height: 14px;
    text-align: center;
  }
  .t-blue { color: var(--sky); }
  .t-orange { color: var(--orange); }

  .headline {
    position: absolute;
    font-weight: 900; font-style: italic;
    font-size: 15.5px; line-height: 19px;
    letter-spacing: 0.1px;
    white-space: nowrap;
  }

  .cta {
    position: absolute;
    background: var(--red); color: var(--white);
    border-radius: 14px;
    display: flex; align-items: center; justify-content: center;
    font-weight: 900; font-size: 13.5px; letter-spacing: 0.8px;
    box-shadow: 0 2px 4px rgba(0,0,0,0.25);
    z-index: 3;
  }
  .cta--italic { font-style: italic; letter-spacing: 0; font-size: 12.5px; font-weight: 700; }

  .rule { position: absolute; left: 0; right: 0; height: 3px; background: var(--white); }

  .photo-tutor {
    position: absolute;
    background: linear-gradient(135deg, #e9ecef 0%, #c9d3df 35%, #7d8fb0 60%, #e6e6e6 100%);
  }
  .photo-kids {
    position: absolute;
    background: linear-gradient(180deg, rgba(246,230,42,0) 0%, rgba(210,215,225,0.75) 35%, #2f4a5e 75%, #1f3b32 100%);
  }

  .logo-cap { position: absolute; background: var(--white); }
  .bullets { position: absolute; list-style: none; font-weight: 900; font-style: italic; font-size: 14px; line-height: 22px; white-space: nowrap; }
  .bullets li::before { content: "• "; color: var(--sky); }
</style>
</head>
<body>

<!-- Vertical rectangle 240 x 400 -->
<section class="banner banner--vertical">
  <div class="logo-tab" style="left:65px;">
    <span class="brand brand--center" style="top:31px; font-size:12px;">Kestrel Study</span>
    <p class="tagline t-blue" style="top:63px;">ONE ON ONE</p>
    <p class="tagline t-orange" style="top:77px;">TUTORING</p>
  </div>
  <p class="headline t-blue" style="left:0; right:0; top:138px; text-align:center;">START YOUR</p>
  <p class="headline t-orange" style="left:0; right:0; top:157px; text-align:center;">CHILD'S PATH TO SUCCESS!</p>
  <div class="photo-tutor" style="left:0; top:215px; width:241px; height:186px;" role="img" aria-label="Tutor and girl working together at a desk in front of a bookshelf"></div>
  <div class="rule" style="top:213px;"></div>
  <div class="cta" style="left:64px; top:198px; width:114px; height:34px;">START NOW</div>
</section>

<!-- Square 250 x 250 -->
<section class="banner banner--square">
  <p class="headline t-blue" style="left:0; right:0; top:16px; text-align:center;">START YOUR</p>
  <p class="headline t-orange" style="left:0; right:0; top:35px; text-align:center;">CHILD'S PATH TO SUCCESS!</p>
  <div class="photo-tutor" style="left:0; top:82px; width:251px; height:168px;" role="img" aria-label="Tutor smiling at a schoolboy in a study room"></div>
  <div class="rule" style="top:80px;"></div>
  <div class="cta" style="left:68px; top:63px; width:114px; height:34px;">START NOW</div>
  <div class="logo-cap" style="left:82px; top:205px; width:100px; height:100px; border-radius:50%;"></div>
  <span class="brand" style="left:82px; width:100px; text-align:center; top:224px; font-size:12px;">Kestrel Study</span>
</section>

<!-- Medium rectangle 300 x 250 -->
<section class="banner banner--medium">
  <div class="photo-kids" style="left:14px; top:95px; width:276px; height:155px;" role="img" aria-label="Smiling group of schoolchildren in uniforms"></div>
  <div class="rule" style="top:221px;"></div>
  <div class="logo-tab" style="left:30px;">
    <span class="brand brand--center" style="top:31px; font-size:12px;">Kestrel Study</span>
    <p class="tagline t-blue" style="top:63px;">ONE ON ONE</p>
    <p class="tagline t-orange" style="top:77px;">TUTORING</p>
  </div>
  <p class="headline t-blue" style="right:20px; top:22px; text-align:right;">START YOUR</p>
  <p class="headline t-orange" style="right:20px; top:44px; text-align:right;">CHILD'S PATH TO</p>
  <p class="headline t-orange" style="right:20px; top:66px; text-align:right;">SUCCESS!</p>
  <div class="cta cta--italic" style="left:172px; top:205px; width:114px; height:33px;">Find Out More</div>
</section>

<!-- Mobile leaderboard 320 x 50 -->
<section class="banner banner--mobile">
  <div class="rule" style="top:27px;"></div>
  <p class="headline" style="left:8px; top:5px; font-size:13px; line-height:16px;"><span class="t-blue">• The Best</span> <span class="t-orange">Tutor For Your Child</span></p>
  <div class="cta cta--italic" style="left:52px; top:26px; width:115px; height:30px; border-radius:10px; align-items:flex-start; padding-top:4px;">Find Out More</div>
  <div class="logo-cap" style="left:214px; top:0; width:120px; height:50px; border-radius:40px 0 0 0;"></div>
  <span class="brand" style="left:228px; width:86px; text-align:center; top:27px; font-size:11.5px;">Kestrel Study</span>
</section>

<!-- Banner 468 x 60 -->
<section class="banner banner--standard">
  <div class="rule" style="top:29px;"></div>
  <div class="logo-cap" style="left:0; top:0; width:133px; height:60px; border-radius:0 60px 0 0;"></div>
  <span class="brand" style="left:14px; top:31px; font-size:12px;">Kestrel Study</span>
  <p class="headline t-blue" style="right:153px; top:9px; font-size:13px; line-height:16px;">START YOUR</p>
  <p class="headline t-orange" style="right:153px; top:36px; font-size:13px; line-height:16px;">CHILD'S PATH TO SUCCESS!</p>
  <div class="cta" style="left:342px; top:13px; width:114px; height:33px;">START NOW</div>
</section>

<!-- Leaderboard 728 x 90 -->
<section class="banner banner--leader">
  <div class="rule" style="top:4px;"></div>
  <div class="rule" style="top:83px;"></div>
  <div class="photo-kids" style="left:468px; top:4px; width:265px; height:86px;" role="img" aria-label="Smiling group of schoolchildren in uniforms"></div>
  <div class="logo-cap" style="left:0; top:0; width:134px; height:90px; border-radius:0 60px 60px 0;"></div>
  <span class="brand" style="left:12px; top:44px; font-size:16px;">Kestrel Study</span>
  <ul class="bullets" style="left:171px; top:12px;">
    <li><span class="t-blue">One on One</span> <span class="t-orange">tutoring at your home</span></li>
    <li><span class="t-orange">Experienced</span> <span class="t-blue">TUTORS</span></li>
    <li><span class="t-blue">The Best</span> <span class="t-orange">Tutor For Your Child</span></li>
  </ul>
  <div class="cta cta--italic" style="left:406px; top:14px; width:53px; height:64px; border-radius:10px; text-align:center; line-height:15px; font-size:12.5px;">Find<br>Out<br>More</div>
</section>

</body>
</html>
```